Logo, Web and Mobile Designs for enterprise social media platform

All the details are in the attached document, please start reading the scope document first which explains what is this project about and the details about the needed deliverables, after that please read the UI_Requirements document which will detail what is expected regarding the coded web version since this is a coded contest, it is very important that you meet the UI requirements or suggest something else but we will need to agree first before working on the coded version

Good Luck

Target Market(s)

Enterprise Social Media

Industry/Entity Type

Media

Coding

Coded - Design and coding required

Number of Pages Required

5+ page

Font styles to use
Sans Serif

Requirements
Must have
• All the must haves are listed in the scope document so please check before you start

```html
<!DOCTYPE html>
<html lang="en">
<head>
<meta charset="utf-8">
<title>Tandemly</title>
<link href="https://fonts.googleapis.com/css2?family=Roboto:wght@300;400;500;700&display=swap" rel="stylesheet">
<style>
:root{
  --blue:#5fb4f2;
  --blue-soft:#a9d2f1;
  --ink:#333;
  --muted:#9a9a9a;
  --line:#e3e3e3;
  --page:#f4f4f4;
  --form-bg:#ebe7e3;
  --panel-bg:#f3f2f1;
  --white:#fff;
}
*{box-sizing:border-box;margin:0;padding:0}
html,body{width:1200px;height:3586px;overflow:hidden}
body{position:relative;font-family:'Roboto',sans-serif;color:var(--ink);background:var(--white)}
.abs{position:absolute}

/* login */
.login{left:0;top:0;width:1200px;height:748px;background:linear-gradient(180deg,#7ea7c4 0%,#5a7f9c 35%,#34495b 70%,#1c2833 100%)}
.login-title{left:0;width:1200px;top:220px;text-align:center;color:var(--white);font-weight:300;font-size:46px;letter-spacing:1px}
.login-input{left:461px;width:278px;height:53px;border:1px solid rgba(255,255,255,.6);color:rgba(255,255,255,.85);font-size:20px;font-weight:300;padding:13px 16px}
.login-forgot{left:0;width:1200px;top:436px;text-align:center;color:rgba(255,255,255,.85);font-size:14px;font-weight:300}
.btn-login{left:468px;top:466px;width:114px;height:48px;color:var(--white);font-size:21px;display:flex;align-items:center;justify-content:center}
.btn-signup{left:605px;top:466px;width:134px;height:48px;background:var(--blue);color:var(--white);font-size:21px;display:flex;align-items:center;justify-content:center}

/* sign up */
.signup-bar{left:0;top:820px;width:1200px;height:84px;background:var(--blue);color:var(--white);font-size:44px;font-weight:300;text-align:center;line-height:84px}
.signup-bar span{color:rgba(255,255,255,.6)}
.steps{left:40px;top:940px;width:1120px;height:28px}
.steps-line{left:0;top:14px;width:1120px;height:1px;background:#d8d8d8}
.step{top:0;display:flex;align-items:center;gap:8px;background:var(--white);padding:0 8px;font-size:14px;color:var(--muted)}
.step i{width:20px;height:20px;border-radius:50%;background:#c9c9c9;color:#fff;font-style:normal;font-size:12px;display:flex;align-items:center;justify-content:center}
.step.active{color:var(--ink);font-weight:500}
.step.active i{background:var(--blue)}
.form-card{left:41px;top:1004px;width:339px;height:526px;background:var(--form-bg)}
.field{left:0;width:339px;height:32px;display:flex;align-items:center}
.field label{width:146px;text-align:right;font-size:14px;color:var(--muted);padding-right:22px}
.field.filled label{color:var(--ink);font-weight:500}
.field .box{width:142px;height:30px;background:var(--white);font-size:11px;color:#bbb;padding:0 8px;display:flex;align-items:center}
.field.filled .box{color:var(--ink);border:1px solid var(--blue-soft)}
.field .split{display:flex;gap:5px}
.field .split .box{width:44px}
.radio{font-size:11px;color:var(--muted);display:flex;gap:12px;align-items:center}
.radio b{display:inline-block;width:8px;height:8px;border-radius:50%;background:var(--blue);margin-right:4px}
.radio em{display:inline-block;width:8px;height:8px;border-radius:50%;border:1px solid #ccc;margin-right:4px}
.radio .on{color:var(--ink)}
.phone-note{left:210px;top:1358px;width:142px;font-size:9px;color:var(--muted);line-height:1.3}
.btn-next{left:41px;top:1446px;width:339px;height:84px;background:var(--blue);color:var(--white);font-size:38px;font-weight:300;display:flex;align-items:center;justify-content:flex-end;padding-right:28px;gap:8px}
.panel{top:1004px;height:526px;background:var(--panel-bg);display:flex;align-items:center;justify-content:center;text-align:center;color:var(--blue-soft);font-size:38px;font-weight:300;line-height:1}

/* app */
.nav{left:0;top:1642px;width:1200px;height:82px;background:var(--blue);color:var(--white)}
.brand{left:34px;top:0;line-height:82px;font-size:21px;font-weight:700}
.nav-links{right:34px;top:0;height:82px;display:flex;align-items:center;gap:22px;font-size:22px;font-weight:400}
.hero{left:0;top:1724px;width:1200px;height:399px;background:linear-gradient(135deg,#4a3a2e 0%,#8a6a50 35%,#b49478 60%,#5a4638 100%)}
.btn-create{left:483px;top:1898px;width:232px;height:48px;background:var(--blue);color:var(--white);font-size:30px;font-weight:300;display:flex;align-items:center;justify-content:center}
.search{left:0;top:2123px;width:1200px;height:71px;background:#fafafa;border-bottom:1px solid var(--line)}
.search-field{left:36px;top:0;height:71px;display:flex;align-items:center;gap:28px;color:#c5c5c5;font-size:32px;font-style:italic;font-weight:300}
.search-select{left:1013px;top:0;width:187px;height:71px;border-left:1px solid var(--line);display:flex;align-items:center;justify-content:center;gap:18px;color:#c5c5c5;font-size:28px;font-style:italic;font-weight:300}
.browse{left:0;top:2194px;width:1200px;height:1310px;background:var(--page)}
.browse-title{left:0;width:1200px;top:2226px;text-align:center;color:var(--blue);font-size:27px;font-weight:400}
.tag{top:2297px;height:36px;border-radius:18px;background:#e2e2e2;display:flex;align-items:center;justify-content:space-between;padding:0 8px 0 18px;font-size:17px;color:#555}
.tag i{width:24px;height:24px;border-radius:50%;background:#a8a8a8;display:flex;align-items:center;justify-content:center}
.filters{left:19px;top:2366px}
.filter{display:flex;align-items:center;gap:12px;height:42px;font-size:14px;color:var(--muted)}
.filter b{width:20px;height:20px;border:1px solid #c8c8c8;background:var(--white);display:flex;align-items:center;justify-content:center}
.filter.on b{background:#b5b5b5;border-color:#b5b5b5}
.grid{left:189px;top:2367px;display:grid;grid-template-columns:repeat(3,264px);grid-auto-rows:339px;column-gap:14px;row-gap:15px}
.card{background:var(--white);display:flex;flex-direction:column}
.card-photo{height:182px}
.card-body{height:95px;padding:14px 12px 0 12px;position:relative}
.card-title{font-size:25px;font-weight:300;color:var(--blue);white-space:nowrap;display:flex;justify-content:space-between;align-items:center}
.card-title span{font-size:30px;font-weight:300}
.card-text{display:flex;justify-content:space-between;gap:6px;margin-top:6px;font-size:12px;color:var(--muted);line-height:1.25}
.card-text p{width:146px}
.card-text a{color:var(--blue);text-decoration:none;align-self:flex-end;white-space:nowrap}
.card-actions{flex:1;display:flex;border-top:1px solid #eee}
.card-actions div{flex:1;display:flex;align-items:center;justify-content:center;font-size:14px}
.card-actions .share{color:var(--blue);border-right:1px solid #eee}
.card-actions .invite{color:var(--muted)}
.card.selected .card-body,.card.selected .card-actions{background:var(--blue)}
.card.selected .card-title,.card.selected .card-text,.card.selected .card-text a,.card.selected .card-title span{color:var(--white)}
.card.selected .card-title{font-weight:400}
.card.selected .share{color:var(--white);border-right-color:rgba(255,255,255,.4)}
.card.selected .invite{color:rgba(255,255,255,.7)}
.card.selected .card-actions{border-top-color:rgba(255,255,255,.4)}
.footer{left:0;top:3504px;width:1200px;height:82px;background:var(--blue);color:var(--white);font-size:21px}
.footer .brand span{font-weight:300}
.footer-note{left:510px;top:0;line-height:82px;font-weight:300}
</style>
</head>
<body>

<section class="login abs" role="img" aria-label="Blurred mountain valley landscape under a blue sky"></section>
<h1 class="login-title abs">TANDEMLY</h1>
<div class="login-input abs" style="top:313px">username or e-mail</div>
<div class="login-input abs" style="top:375px">password</div>
<p class="login-forgot abs">Forgot your password or username ?</p>
<div class="btn-login abs">LOGIN</div>
<div class="btn-signup abs">SIGN UP</div>

<header class="signup-bar abs">TANDEMLY <span>sign up</span></header>
<div class="steps abs">
  <div class="steps-line abs"></div>
  <div class="step active abs" style="left:0"><i>1</i>Personal info</div>
  <div class="step abs" style="left:494px"><i>2</i>Company info</div>
  <div class="step abs" style="right:0"><i>3</i>Finish</div>
</div>

<form class="form-card abs">
  <div class="field abs" style="top:60px"><label>Name</label><div class="box">Enter your name</div></div>
  <div class="field filled abs" style="top:96px"><label>Surname</label><div class="box">Doe</div></div>
  <div class="field abs" style="top:134px"><label>Birthday</label><div class="split"><div class="box">Mm</div><div class="box">Dd</div><div class="box">Yyyy</div></div></div>
  <div class="field abs" style="top:170px"><label>Gender</label><div class="radio"><span class="on"><b></b>Female</span><span><em></em>Male</span></div></div>
  <div class="field abs" style="top:208px"><label>E-mail</label><div class="box">Enter your e-mail</div></div>
  <div class="field abs" style="top:246px"><label>Password</label><div class="box">Enter a password</div></div>
  <div class="field filled abs" style="top:284px"><label>Confirm Password</label><div class="box">•••••••••</div></div>
  <div class="field abs" style="top:323px"><label>Phone Number</label><div class="box">
    <svg width="34" height="14" viewBox="0 0 34 14"><rect width="22" height="14" fill="#c33"/><rect y="2" width="22" height="2" fill="#fff"/><rect y="6" width="22" height="2" fill="#fff"/><rect y="10" width="22" height="2" fill="#fff"/><rect width="10" height="7" fill="#2b4a8c"/><path d="M26 5l3 4 3-4z" fill="#555"/></svg>
    <span style="margin-left:6px">000 00 0000</span></div></div>
</form>
<p class="phone-note abs">We will use your phone number to send a confirmation code</p>
<div class="btn-next abs">NEXT <svg width="20" height="34" viewBox="0 0 20 34"><path d="M3 3l14 14L3 31" fill="none" stroke="#fff" stroke-width="3"/></svg></div>
<div class="panel abs" style="left:430px;width:337px">COMPANY<br>INFO</div>
<div class="panel abs" style="left:820px;width:339px">FINISH</div>

<nav class="nav abs">
  <div class="brand abs">TANDEMLY</div>
  <div class="nav-links abs">
    <span>HOME</span><span>EVENTS</span><span>GROUPS</span><span>BUSINESS</span><span>ABOUT</span>
    <svg width="22" height="22" viewBox="0 0 24 24"><circle cx="12" cy="12" r="7" fill="none" stroke="#fff" stroke-width="5" stroke-dasharray="3 2.5"/><circle cx="12" cy="12" r="4" fill="#fff"/><circle cx="12" cy="12" r="2" fill="#5fb4f2"/></svg>
    <svg width="20" height="20" viewBox="0 0 20 20"><circle cx="10" cy="6" r="5" fill="#fff"/><path d="M0 20c0-6 4-8 10-8s10 2 10 8z" fill="#fff"/></svg>
  </div>
</nav>
<div class="hero abs" role="img" aria-label="Meeting table with notebooks, iced drinks and a laptop"></div>
<div class="btn-create abs">Create event</div>
<div class="search abs">
  <div class="search-field abs"><svg width="40" height="40" viewBox="0 0 40 40"><circle cx="16" cy="16" r="12" fill="none" stroke="#d2d2d2" stroke-width="3"/><path d="M25 25l12 12" stroke="#d2d2d2" stroke-width="3"/></svg>Search</div>
  <div class="search-select abs">Events <svg width="16" height="10" viewBox="0 0 16 10"><path d="M1 1l7 7 7-7" fill="none" stroke="#ccc" stroke-width="2"/></svg></div>
</div>

<section class="browse abs"></section>
<h2 class="browse-title abs">BROWSE EVENTS</h2>
<div class="tag abs" style="left:191px;width:144px">Banking<i><svg width="10" height="10" viewBox="0 0 10 10"><path d="M1 1l8 8M9 1l-8 8" stroke="#fff" stroke-width="2"/></svg></i></div>
<div class="tag abs" style="left:351px;width:144px">Trading<i><svg width="10" height="10" viewBox="0 0 10 10"><path d="M1 1l8 8M9 1l-8 8" stroke="#fff" stroke-width="2"/></svg></i></div>
<div class="tag abs" style="left:509px;width:172px">Production<i><svg width="10" height="10" viewBox="0 0 10 10"><path d="M1 1l8 8M9 1l-8 8" stroke="#fff" stroke-width="2"/></svg></i></div>

<ul class="filters abs" style="list-style:none">
  <li class="filter"><b></b>Construction</li>
  <li class="filter"><b></b>Metal</li>
  <li class="filter"><b></b>Jewlery</li>
  <li class="filter"><b></b>Transport</li>
  <li class="filter on"><b><svg width="12" height="10" viewBox="0 0 12 10"><path d="M1 5l3.5 3.5L11 1" fill="none" stroke="#fff" stroke-width="2"/></svg></b>Banking</li>
  <li class="filter on"><b><svg width="12" height="10" viewBox="0 0 12 10"><path d="M1 5l3.5 3.5L11 1" fill="none" stroke="#fff" stroke-width="2"/></svg></b>Trading</li>
  <li class="filter on"><b><svg width="12" height="10" viewBox="0 0 12 10"><path d="M1 5l3.5 3.5L11 1" fill="none" stroke="#fff" stroke-width="2"/></svg></b>Production</li>
</ul>

<div class="grid abs">
  <article class="card"><div class="card-photo" style="background:linear-gradient(135deg,#5a5550,#b8ada0)" role="img" aria-label="People working at a desk with laptop and coffee"></div>
    <div class="card-body"><div class="card-title">a-Prod hiring...<span>+</span></div><div class="card-text"><p>a-Prod is hiring with an open and form...</p><a>READ MORE</a></div></div>
    <div class="card-actions"><div class="share">SHARE</div><div class="invite">INVITE</div></div></article>
  <article class="card"><div class="card-photo" style="background:linear-gradient(135deg,#3a3f44,#8c8a80)" role="img" aria-label="Partners meeting in a booth"></div>
    <div class="card-body"><div class="card-title">n-Bank partner...<span>+</span></div><div class="card-text"><p>n-Bank partner meeting is taking place...</p><a>READ MORE</a></div></div>
    <div class="card-actions"><div class="share">SHARE</div><div class="invite">INVITE</div></div></article>
  <article class="card"><div class="card-photo" style="background:linear-gradient(135deg,#4a2f24,#8a5a44)" role="img" aria-label="Team at a wooden table with notebooks"></div>
    <div class="card-body"><div class="card-title">x-Trade meet...<span>+</span></div><div class="card-text"><p>x-Trade is throwing a meeting for...</p><a>READ MORE</a></div></div>
    <div class="card-actions"><div class="share">SHARE</div><div class="invite">INVITE</div></div></article>

  <article class="card"><div class="card-photo" style="background:linear-gradient(180deg,#2a2a2a,#9a9a9a)" role="img" aria-label="People looking out of large office windows in black and white"></div>
    <div class="card-body"><div class="card-title">GamaProd is sell...<span>+</span></div><div class="card-text"><p>GamaProd is selling used material...</p><a>READ MORE</a></div></div>
    <div class="card-actions"><div class="share">SHARE</div><div class="invite">INVITE</div></div></article>
  <article class="card selected"><div class="card-photo" style="background:linear-gradient(135deg,#7a3a2a,#c29a78)" role="img" aria-label="Table with coffee cups and tablet in front of a brick wall"></div>
    <div class="card-body"><div class="card-title">Trade partners...<span><svg width="22" height="18" viewBox="0 0 22 18"><path d="M2 9l6 6L20 2" fill="none" stroke="#fff" stroke-width="2.5"/></svg></span></div><div class="card-text"><p>Trade partners are meeting to discuss...</p><a>READ MORE</a></div></div>
    <div class="card-actions"><div class="share">SHARE</div><div class="invite">INVITE</div></div></article>
  <article class="card"><div class="card-photo" style="background:linear-gradient(180deg,#e8e8e8,#555)" role="img" aria-label="Business people walking in black and white"></div>
    <div class="card-body"><div class="card-title">Twin markets...<span>+</span></div><div class="card-text"><p>Twin markets as a leading company...</p><a>READ MORE</a></div></div>
    <div class="card-actions"><div class="share">SHARE</div><div class="invite">INVITE</div></div></article>

  <article class="card"><div class="card-photo" style="background:linear-gradient(135deg,#f2f2f2,#b0b0b0)" role="img" aria-label="White desk with tablet and coffee cup"></div>
    <div class="card-body"><div class="card-title">Brand &amp; repres...<span>+</span></div><div class="card-text"><p>An business open discussion about...</p><a>READ MORE</a></div></div>
    <div class="card-actions"><div class="share">SHARE</div><div class="invite">INVITE</div></div></article>
  <article class="card"><div class="card-photo" style="background:linear-gradient(135deg,#3a5a5a,#b89a80)" role="img" aria-label="Audience attending a business lecture"></div>
    <div class="card-body"><div class="card-title">Business lect...<span>+</span></div><div class="card-text"><p>Business succesful stories are about...</p><a>READ MORE</a></div></div>
    <div class="card-actions"><div class="share">SHARE</div><div class="invite">INVITE</div></div></article>
  <article class="card"><div class="card-photo" style="background:linear-gradient(135deg,#8a6a50,#d8c8b0)" role="img" aria-label="Hand holding a smartphone over a wooden table"></div>
    <div class="card-body"><div class="card-title">Social media...<span>+</span></div><div class="card-text"><p>Social media is helping businesses...</p><a>READ MORE</a></div></div>
    <div class="card-actions"><div class="share">SHARE</div><div class="invite">INVITE</div></div></article>
</div>

<footer class="footer abs">
  <div class="brand abs">TANDEMLY <span>l.l.c</span></div>
  <div class="footer-note abs">All rights reserved</div>
</footer>

</body>
</html>
```